High end Electrical/home automation Business Card

Need a card for a high end electrical and home automation company utilising the existing logo.
Phone
Email
Website

Like black look with raised detail. Don’t necessarily need to keep colour of logo it could be made grayscale or white etc

Target Market(s)

High end clients

Contact Information for Business Card

Northwell Electrical

Requirements
Must have
• Logo, phone, email, website, address

High end look
Nice to have
• Black background card
Raised font
Should not have
• Lots of colour

```html
<!DOCTYPE html>
<html lang="en">
<head>
<meta charset="utf-8">
<title>Northwell Electrical – Business Card</title>
<link href="https://fonts.googleapis.com/css2?family=Roboto:wght@400;700&display=swap" rel="stylesheet">
<style>
  :root {
    --bg: #e6e6e4;
    --card-white: #ffffff;
    --card-dark: #2c2d31;
    --accent: #1a8fd6;
    --ink: #2b2b2b;
    --ink-soft: #555555;
    --silver: #b9babd;
  }
  * { margin: 0; padding: 0; box-sizing: border-box; }
  html, body {
    width: 1200px; height: 801px; overflow: hidden;
    background: var(--bg);
    font-family: "Roboto", Arial, sans-serif;
  }
  .stage {
    position: relative; width: 1200px; height: 801px;
    display: flex; align-items: center; justify-content: center; gap: 60px;
  }
  .card {
    position: relative; width: 520px; height: 297px;
    border-bottom: 5px solid var(--accent);
    box-shadow: 0 10px 24px rgba(0,0,0,0.18);
  }
  .card--front { background: var(--card-white); }
  .card--back { background: var(--card-dark); }

  .brand {
    position: absolute; top: 42px; right: 44px;
    display: flex; align-items: center; gap: 10px;
    font-weight: 700; font-size: 24px; letter-spacing: -0.5px;
    color: var(--ink);
  }
  .brand__dot {
    width: 14px; height: 14px; border-radius: 50%; background: var(--accent);
  }
  .divider {
    position: absolute; left: 40px; right: 40px; top: 140px;
    height: 2px; background: var(--ink);
  }
  .address {
    position: absolute; top: 156px; right: 44px; text-align: right;
    font-size: 13px; line-height: 1.35; color: var(--ink-soft);
  }
  .person { position: absolute; left: 40px; top: 168px; }
  .person__name { font-weight: 700; font-size: 22px; color: var(--accent); }
  .person__role { font-size: 13px; color: var(--ink-soft); margin-top: 2px; }
  .person__rule { width: 150px; height: 1.5px; background: var(--ink); margin: 8px 0 6px; }
  .contacts { list-style: none; font-size: 13.5px; color: var(--ink-soft); }
  .contacts li { display: flex; align-items: center; gap: 9px; line-height: 1.45; }
  .contacts svg { width: 12px; height: 12px; flex: none; }
  .contacts .hl { color: var(--accent); }

  .back-brand {
    position: absolute; right: 44px; bottom: 70px;
    font-weight: 700; font-size: 32px; letter-spacing: -0.5px;
    color: var(--silver);
  }
</style>
</head>
<body>
<main class="stage">
  <section class="card card--front" aria-label="Business card front">
    <div class="brand"><span class="brand__dot"></span>Northwell Electrical</div>
    <div class="divider"></div>
    <p class="address">Your address, city<br>state, ZIP 0000</p>
    <div class="person">
      <p class="person__name">Daniel Hartley</p>
      <p class="person__role">Manager</p>
      <div class="person__rule"></div>
      <ul class="contacts">
        <li>
          <svg viewBox="0 0 12 12"><path d="M3 1 L5 3.5 L4 5 Q5.5 7 7 8 L8.5 7 L11 9 L9.5 11 Q4 10 1 2.5 Z" fill="var(--accent)"/></svg>
          123-456-2100
        </li>
        <li>
          <svg viewBox="0 0 12 12"><rect x="0.8" y="2.5" width="10.4" height="7" fill="none" stroke="var(--accent)" stroke-width="1.2"/><path d="M1 3 L6 6.8 L11 3" fill="none" stroke="var(--accent)" stroke-width="1.2"/></svg>
          youremail@mailbox.com
        </li>
        <li>
          <svg viewBox="0 0 12 12"><circle cx="6" cy="6" r="5" fill="none" stroke="var(--accent)" stroke-width="1.2"/><path d="M1 6 H11 M6 1 Q3 6 6 11 M6 1 Q9 6 6 11" fill="none" stroke="var(--accent)" stroke-width="1"/></svg>
          <span>www.<span class="hl">yourwebsite</span>.com</span>
        </li>
      </ul>
    </div>
  </section>

  <section class="card card--back" aria-label="Business card back">
    <p class="back-brand">Northwell Electrical</p>
  </section>
</main>
</body>
</html>
```